Business card for IT company

Looking for a business card for an IT company providing server, network, and application support to medium businesses. Company name is Calderwick Systems. Website is www.calderwicksystems.example, would like to use the green color that is on the homepage. Prefer design to be done in Illustrator. Please, only DESIGNERS apply - no PHP programmers attempting to do design. Thank you

Industry/Entity Type

Information Technology

Requirements
Must have
• Green
Should not have
• Template designs, or designs done by non-designer type people

```html
<!DOCTYPE html>
<html lang="en">
<head>
<meta charset="utf-8">
<title>Calderwick Systems – Business Card</title>
<link href="https://fonts.googleapis.com/css2?family=Exo+2:wght@400;500&display=swap" rel="stylesheet">
<style>
  :root {
    --bg: #2a2a2a;
    --paper: #ffffff;
    --green: #8cbd2a;
    --green-dark: #6fa51c;
    --green-tile: #7cae2c;
    --purple: #8e4f8f;
    --orange: #e07e0c;
    --yellow: #e3b30a;
    --blue: #1a8fcf;
    --ink-light: #ffffff;
  }
  * { box-sizing: border-box; margin: 0; padding: 0; }
  html, body { width: 1200px; height: 900px; overflow: hidden; }
  body {
    background: var(--bg);
    font-family: "Exo 2", sans-serif;
    position: relative;
  }
  .card {
    position: absolute;
    left: 250px;
    width: 700px;
    height: 400px;
    overflow: hidden;
  }
  /* Front side */
  .card-front {
    top: 35px;
    background: radial-gradient(ellipse at 40% 40%, var(--green) 0%, var(--green-dark) 100%);
    display: flex;
    align-items: center;
    justify-content: center;
    gap: 18px;
  }
  .front-mark {
    width: 46px; height: 46px;
    border-radius: 50%;
    background: rgba(255,255,255,0.9);
  }
  .front-name {
    color: var(--ink-light);
    font-size: 44px;
    font-weight: 400;
    letter-spacing: 4px;
    text-transform: uppercase;
  }
  /* Back side */
  .card-back {
    top: 465px;
    background: var(--paper);
  }
  .tile {
    position: absolute;
    color: var(--ink-light);
    text-transform: uppercase;
    white-space: nowrap;
  }
  .tile-logo {
    left: 30px; top: 40px; width: 125px; height: 100px;
    background: var(--green-tile);
    display: flex; flex-direction: column; align-items: center; justify-content: center; gap: 8px;
  }
  .logo-mark { width: 34px; height: 34px; border-radius: 50%; background: var(--paper); }
  .logo-name { font-size: 12px; letter-spacing: 1px; text-align: center; line-height: 1.2; }
  .tile-person {
    left: 30px; top: 148px; width: 290px; height: 100px;
    background: var(--purple);
    padding: 30px 0 0 22px;
    font-size: 15px;
    letter-spacing: 1px;
    line-height: 1.35;
  }
  .tile-services-a {
    left: 328px; top: 148px; width: 120px; height: 100px;
    background: var(--orange);
    padding: 14px 0 0 14px;
  }
  .tile-contact {
    left: 30px; top: 256px; width: 418px; height: 104px;
    background: var(--blue);
  }
  .contact-list { list-style: none; position: absolute; left: 18px; bottom: 14px; }
  .contact-list li { display: flex; align-items: center; gap: 10px; font-size: 15px; letter-spacing: 0.5px; line-height: 1.4; }
  .contact-list svg { width: 15px; height: 15px; fill: var(--ink-light); flex: none; }
  .tile-accent {
    left: 456px; top: 148px; width: 90px; height: 76px;
    background: var(--yellow);
  }
  .tile-services-b {
    left: 554px; top: 148px; width: 126px; height: 76px;
    background: var(--blue);
    padding: 7px 0 0 12px;
  }
  .service-list { list-style: none; font-size: 10px; letter-spacing: 0.3px; line-height: 1.25; }
  .tile-address {
    left: 456px; top: 232px; width: 224px; height: 128px;
    background: var(--green-tile);
    padding: 38px 0 0 14px;
    font-size: 10.5px;
    line-height: 1.5;
  }
</style>
</head>
<body>
  <section class="card card-front" aria-label="Card front">
    <span class="front-mark"></span>
    <h1 class="front-name">Calderwick Systems</h1>
  </section>

  <section class="card card-back" aria-label="Card back">
    <div class="tile tile-logo">
      <span class="logo-mark"></span>
      <span class="logo-name">Calderwick<br>Systems</span>
    </div>

    <div class="tile tile-person">
      <p>Daniel Harwick</p>
      <p>Managing Director</p>
    </div>

    <div class="tile tile-services-a">
      <ul class="service-list">
        <li>Networking</li>
        <li>Servers</li>
        <li>Databases</li>
        <li>Backup</li>
        <li>and Restore</li>
      </ul>
    </div>

    <div class="tile tile-contact">
      <ul class="contact-list">
        <li><svg viewBox="0 0 16 16"><path d="M2 6c0-2 2-3 6-3s6 1 6 3v1h-3V5.5H5V7H2z M4 8h8l1 5H3z"/></svg>800 555 01 20</li>
        <li><svg viewBox="0 0 16 16"><path d="M5 1h6a1 1 0 0 1 1 1v12a1 1 0 0 1-1 1H5a1 1 0 0 1-1-1V2a1 1 0 0 1 1-1zm0 2v9h6V3z"/></svg>800 555 01 21</li>
        <li><svg viewBox="0 0 16 16"><path d="M1 4h14v9H1z M1.5 4.5 8 9l6.5-4.5" stroke="#1a8fcf" stroke-width="1"/></svg>d.harwick@calderwicksystems.example</li>
      </ul>
    </div>

    <div class="tile tile-accent"></div>

    <div class="tile tile-services-b">
      <ul class="service-list">
        <li>Virus / Malware</li>
        <li>Deployment</li>
        <li>File Services</li>
        <li>Software</li>
        <li>Hardware</li>
      </ul>
    </div>

    <div class="tile tile-address">
      <p>48 Example Lane</p>
      <p>Millbrook, NY 10001</p>
      <p>www.calderwicksystems.example</p>
    </div>
  </section>
</body>
</html>
```